Give Tall Oak Ridge an Online Presence!

Tall Oak Ridge Property Maintenance is an Australian Owned property maintenance company who needs a stand out online presence.

TOR maintains many buildings and sites and wants to appeal to a corporate professional market with their brand new website. TOR is essentially a handyman service offering all maintenance services to home owners, office managers, real estate agents and strata managers.

The Website:
We need a corporate website that appeals to our broader customer base (property owners, property managers, office managers) the copy is being written by a professional so use filler text for now.

Things that we want:
Home page that sets us apart and appeals to the corporate and residential market. The home page needs to not focus on either the residential or commercial market. The home page should focus on our logo and branding. We have a logo already and it is attached to the brief, please use it and try to consider the colour pallette that goes with it. Whilst we want the site to appear strong and manly it is important to remember that 95% of our customers are female so we need the site to be appealing to women. Women need to believe that we are strong, dependable and trustworthy.
We'd like a quote page and potentially also the ability to get a quote from the home page (please don't put it in if it ruins the overall feel of the home page)
An "about us" page
A contact us page
A blog that's built in (we don't want to link to an external blog)
(overall we'd expect to have 6 or 7 pages total)

The site will also need coding - we expect this to be done in a separate project but need you to consider a few things about the coding side of things.

It needs to be iPhone and iPad compatible.

We'd like you to suggest the best CMS that you would use or if you would suggest not using a CMS please let us know with your submissions.

Target Market(s)

Property owners, office managers and property managers who need maintenance on buildings (So all of them)

Industry/Entity Type

Property Maintenance

Requirements
Must have
• Our Logo
Home page
About Us
Residential
Commercial
Real Estate/Strata
Contact Us/Quote
Blog
Nice to have
• Quote form included in home page
Movement on the home page at least
Should not have
• other logos, too much colour
NO FLASH

```html
<!DOCTYPE html>
<html lang="en">
<head>
<meta charset="utf-8">
<title>Tall Oak Ridge Property Maintenance</title>
<link rel="stylesheet" href="https://fonts.googleapis.com/css2?family=PT+Sans+Narrow:wght@400;700&family=Open+Sans:wght@400&display=swap">
<style>
:root{
  --dark:#363231;
  --darker:#2a2726;
  --blue:#45bde8;
  --band:#4cc1e9;
  --text:#4a4a4a;
  --page:#e9edf0;
  --panel:#ffffff;
  --box:#f5f5f5;
  --line:#d6d6d6;
  --orange:#f28a1d;
  --green:#c4f02a;
}
*{margin:0;padding:0;box-sizing:border-box}
html,body{width:1200px;height:1080px;overflow:hidden}
body{position:relative;background:var(--page);font-family:"PT Sans Narrow",sans-serif;color:var(--text)}
.abs{position:absolute}

.topbar{left:0;top:0;width:1200px;height:118px;background:var(--dark);border-top:5px solid var(--darker);box-shadow:0 2px 4px rgba(0,0,0,.25)}
.nav{left:171px;top:46px;font-weight:700;font-size:18px;color:#e4e4e4;letter-spacing:.2px}
.nav span{position:absolute;white-space:nowrap}
.nav .active{color:var(--blue)}
.auth{top:49px;height:24px;background:linear-gradient(#ffffff,#e6e6e6);border:1px solid #cfcfcf;color:var(--blue);font-family:"Open Sans",sans-serif;font-size:12px;line-height:22px;text-align:center;letter-spacing:.5px}

.hero{left:0;top:118px;width:1200px;height:342px;background:radial-gradient(ellipse 640px 380px at 380px 170px,#ffffff 0%,#f3f6f8 30%,#e6ebef 60%,#dfe5ea 100%)}
.hero-rays{left:0;top:118px;width:1200px;height:342px}
.logo{left:262px;top:300px;display:flex;align-items:center;gap:10px}
.logo-square{width:22px;height:22px;background:var(--orange)}
.logo-name{font-weight:700;font-size:24px;color:var(--orange);line-height:1.05;width:220px}
.headline{left:633px;top:186px;font-weight:700;font-size:43px;line-height:47px;color:#363231;letter-spacing:.5px}
.subline{left:634px;top:292px;font-size:21px;color:var(--blue);letter-spacing:.3px}
.hero-copy{left:634px;top:342px;width:345px;font-size:12px;line-height:19px;color:#555}
.pointer{left:982px;top:345px;width:58px;height:124px;border-radius:30px 30px 10px 30px;background:linear-gradient(160deg,#e4fb7a 0%,var(--green) 55%,#a6d915 100%);opacity:.9}

.band{left:0;top:460px;width:1200px;height:72px;background:var(--band);border-bottom:2px solid #8fd3ee}
.band-title{left:187px;top:471px;font-weight:700;font-size:21px;color:#2f2f2f}
.band-copy{left:187px;top:499px;font-family:"Open Sans",sans-serif;font-size:12.5px;color:#2f3a40;letter-spacing:.6px}
.cta{left:822px;top:477px;width:171px;height:37px;background:var(--dark);color:#fff;font-size:15px;line-height:37px;text-align:center}

.panel{left:154px;top:533px;width:892px;height:547px;background:var(--panel)}
.intro-title{left:184px;top:563px;font-weight:700;font-size:22px;color:var(--blue);letter-spacing:1px}
.intro-rule{left:184px;top:596px;width:528px;height:1px;background:var(--line)}
.intro-copy{left:185px;top:600px;width:530px;font-size:14.5px;line-height:24px;color:#555}
.read-more{font-family:"Open Sans",sans-serif;font-size:11.5px;color:var(--blue)}
.intro-more{left:185px;top:681px;font-family:"PT Sans Narrow",sans-serif;font-size:14px}
.video{left:753px;top:565px;width:266px;height:153px;border:1px solid #e1e1e1;background:#fff;box-shadow:0 0 3px rgba(0,0,0,.08)}
.video-still{position:absolute;left:9px;top:9px;width:246px;height:134px;background:linear-gradient(100deg,#2d5a9a 0%,#3a64a0 30%,#c9a48a 55%,#e9e4e0 80%,#d9d2cc 100%)}
.play{position:absolute;left:100px;top:33px}

.feature{top:748px;width:196px;height:245px;background:var(--box);border:1px solid #dcdcdc}
.feature-head{height:35px;background:repeating-linear-gradient(135deg,#2e2b2a 0 2px,#383433 2px 4px);color:#fff;font-family:"Open Sans",sans-serif;font-size:15.5px;line-height:35px;text-align:center;letter-spacing:.5px}
.gear{display:block;margin:19px auto 0}
.feature-copy{margin-top:14px;padding:0 16px;font-family:"Open Sans",sans-serif;font-size:12px;line-height:22px;color:#3e3e3e;text-align:center}
.feature-more{position:absolute;left:0;width:100%;bottom:16px;text-align:center}

.foot-rule{left:171px;top:1018px;width:857px;height:1px;background:#cfcfcf}
.copyright{left:185px;top:1043px;font-family:"Open Sans",sans-serif;font-size:10.5px;color:#777;letter-spacing:.4px}
.copyright b{font-weight:400;color:var(--blue)}
.social{left:537px;top:1039px;display:flex;gap:16px}
.social span{width:21px;height:21px;border-radius:50%}
.foot-nav{top:1043px;font-family:"Open Sans",sans-serif;font-size:10.5px;color:#777;letter-spacing:.4px}
</style>
</head>
<body>

<header class="abs topbar"></header>
<nav class="abs nav">
  <span class="active" style="left:0">HOME</span>
  <span style="left:75px">ABOUT</span>
  <span style="left:153px">RESIDENTIAL</span>
  <span style="left:273px">COMMERCIAL</span>
  <span style="left:399px">REAL ESTATE</span>
  <span style="left:523px">BLOG</span>
  <span style="left:589px">CONTACT</span>
</nav>
<div class="abs auth" style="left:883px;width:60px">Login</div>
<div class="abs auth" style="left:953px;width:76px">Register</div>

<section class="abs hero" role="img" aria-label="Soft light burst background behind the brand"></section>
<div class="abs logo">
  <span class="logo-square"></span>
  <span class="logo-name">Tall Oak Ridge Property Maintenance</span>
</div>
<h1 class="abs headline">LOREM IPSUM LINER<br>PEPLOEN GERINING OL</h1>
<p class="abs subline">Morem ipsum dolor sit amet consling adertise</p>
<p class="abs hero-copy">Lorem ipsum dolor sit amet, consectetur adipiscing elit. Praesent dolor nunc, rhoncus porttitor bibendum in, placerat sed dui raesent suscipit consequat nu</p>
<div class="abs pointer" role="img" aria-label="Green curved arrow pointing down to the get started button"></div>

<section class="abs band"></section>
<h2 class="abs band-title">Vivamus sit amet magna nec nislo</h2>
<p class="abs band-copy">Lorem ipsum &nbsp;riste &nbsp;turpis euismod quis ullamcorper orci semper mattis porttitor nullaest</p>
<div class="abs cta">GET STARTED</div>

<main class="abs panel"></main>
<h2 class="abs intro-title">LOREM IPSUMING EREDTCE</h2>
<div class="abs intro-rule"></div>
<p class="abs intro-copy">Vestibulum non consectetur urna. Ut non quam quam. Nam congue rutrum leo, vel vulputate nibh mollis vel. Cras eleifend dui eget lectus vehicula eu ornare nunc sodales. Pellentesque habitant morbi tristique senectus et netus et malesuada fames ac turpis egestas. Cras luctus, turpis et semper rhoncus,</p>
<span class="abs read-more intro-more">read more &#9656;</span>
<div class="abs video">
  <div class="video-still" role="img" aria-label="Video still of a tradesman fitting copper pipes to a ceiling">
    <svg class="play" width="68" height="68" viewBox="0 0 68 68">
      <circle cx="34" cy="34" r="33" fill="rgba(50,50,50,.85)"/>
      <path d="M27 22 L48 34 L27 46 Z" fill="#fff"/>
    </svg>
  </div>
</div>

<article class="abs feature" style="left:172px">
  <div class="feature-head">LOREM IPSUM</div>
  <svg class="gear" width="34" height="34" viewBox="0 0 34 34"><circle cx="17" cy="17" r="13" fill="none" stroke="var(--blue)" stroke-width="7" stroke-dasharray="4.5 2.3"/><circle cx="17" cy="17" r="11" fill="var(--blue)"/><circle cx="17" cy="17" r="5" fill="var(--box)"/></svg>
  <p class="feature-copy">Donec tempor, risus eu fring la mattis, quam magna ultrices diam, ac scelerisque est ligula in ante ivamus vestibul</p>
  <span class="read-more feature-more">read more</span>
</article>
<article class="abs feature" style="left:392px">
  <div class="feature-head">LOREM IPSUM</div>
  <svg class="gear" width="34" height="34" viewBox="0 0 34 34"><circle cx="17" cy="17" r="13" fill="none" stroke="var(--blue)" stroke-width="7" stroke-dasharray="4.5 2.3"/><circle cx="17" cy="17" r="11" fill="var(--blue)"/><circle cx="17" cy="17" r="5" fill="var(--box)"/></svg>
  <p class="feature-copy">Donec tempor, risus eu fring la mattis, quam magna ultrices diam, ac scelerisque est ligula in ante ivamus vestibul</p>
  <span class="read-more feature-more">read more</span>
</article>
<article class="abs feature" style="left:612px">
  <div class="feature-head">LOREM IPSUM</div>
  <svg class="gear" width="34" height="34" viewBox="0 0 34 34"><circle cx="17" cy="17" r="13" fill="none" stroke="var(--blue)" stroke-width="7" stroke-dasharray="4.5 2.3"/><circle cx="17" cy="17" r="11" fill="var(--blue)"/><circle cx="17" cy="17" r="5" fill="var(--box)"/></svg>
  <p class="feature-copy">Donec tempor, risus eu fring la mattis, quam magna ultrices diam, ac scelerisque est ligula in ante ivamus vestibul</p>
  <span class="read-more feature-more">read more</span>
</article>
<article class="abs feature" style="left:833px">
  <div class="feature-head">LOREM IPSUM</div>
  <svg class="gear" width="34" height="34" viewBox="0 0 34 34"><circle cx="17" cy="17" r="13" fill="none" stroke="var(--blue)" stroke-width="7" stroke-dasharray="4.5 2.3"/><circle cx="17" cy="17" r="11" fill="var(--blue)"/><circle cx="17" cy="17" r="5" fill="var(--box)"/></svg>
  <p class="feature-copy">Donec tempor, risus eu fring la mattis, quam magna ultrices diam, ac scelerisque est ligula in ante ivamus vestibul</p>
  <span class="read-more feature-more">read more</span>
</article>

<div class="abs foot-rule"></div>
<p class="abs copyright">© 2012 <b>oakframe</b> &nbsp;| &nbsp;All rights reserved</p>
<div class="abs social">
  <span style="background:#1f4f7a" aria-label="Social link"></span>
  <span style="background:#2f7bc0" aria-label="Social link"></span>
  <span style="background:#ee6a2c" aria-label="News feed"></span>
  <span style="background:#b5b5b5" aria-label="Email"></span>
</div>
<span class="abs foot-nav" style="left:815px;color:var(--blue)">Home</span>
<span class="abs foot-nav" style="left:863px">Lorem</span>
<span class="abs foot-nav" style="left:913px">Ipsume</span>
<span class="abs foot-nav" style="left:968px">Contact</span>

</body>
</html>
```